New Innovative Counselling and psychotherapy Service needs Business Card design

Keep it simple and professional. On one side, just company name and logo (perhaps in all blue) and maybe a tag line.

On other side (all white) my name and Qualifications in centre

Industry/Entity Type

Health And Wellness

Contact Information for Business Card

Derek Hollis
Counsellor & Psychotherapist
BSc (Psychol.), BA, Dip. (Couns. & Psych.), PG.Cert (CBT), MGVrA, NWTF

I will also require Mobile no, Email and web site address of which I'll pass on to final designer.

Font styles to use
Sans Serif

Requirements
Must have
• My Logo Only and please use the colours in logo that is in it.
Should not have
• Any other images

```html
<!DOCTYPE html>
<html lang="en">
<head>
<meta charset="utf-8">
<title>Kindred Path – Business Card</title>
<link rel="stylesheet" href="https://fonts.googleapis.com/css2?family=Open+Sans:wght@300;400;600;700&display=swap">
<style>
  :root {
    --stage: #e4e6e8;
    --card-white: #ffffff;
    --brand-blue: #4aaee3;
    --brand-green: #8cc63f;
    --ink: #4a4a4a;
    --ink-soft: #666666;
    --shadow: rgba(0, 0, 0, 0.18);
  }
  * { box-sizing: border-box; margin: 0; padding: 0; }
  html, body {
    width: 1200px; height: 872px; overflow: hidden;
    background: var(--stage);
    font-family: "Open Sans", Arial, sans-serif;
  }
  .stage {
    position: relative; width: 1200px; height: 872px;
    display: flex; align-items: center; justify-content: center; gap: 60px;
  }
  .card {
    width: 520px; height: 320px; position: relative;
    box-shadow: 0 6px 18px var(--shadow);
  }
  .card--front { background: var(--card-white); }
  .card--back { background: var(--brand-blue); color: var(--card-white); }

  .brand { display: flex; align-items: center; gap: 12px; }
  .brand__dot { width: 34px; height: 34px; border-radius: 50%; background: var(--brand-blue); flex: none; }
  .brand__name { font-weight: 400; font-size: 27px; color: var(--ink); letter-spacing: -0.2px; white-space: nowrap; }

  .card--front .brand { position: absolute; left: 48px; top: 40px; }

  .person { position: absolute; left: 48px; top: 116px; right: 40px; }
  .person__name { color: var(--brand-blue); font-weight: 700; font-size: 19px; line-height: 1.2; }
  .person__role { color: var(--ink-soft); font-size: 12px; margin-top: 4px; }
  .person__quals { color: var(--ink-soft); font-size: 11px; margin-top: 2px; white-space: nowrap; }

  .divider { position: absolute; left: 48px; right: 48px; top: 190px; height: 8px; }

  .contact { position: absolute; top: 216px; font-size: 11.5px; color: var(--ink-soft); line-height: 20px; list-style: none; white-space: nowrap; }
  .contact--direct { left: 48px; }
  .contact--address { left: 278px; top: 236px; }
  .contact li { display: flex; align-items: center; gap: 8px; }
  .contact svg { width: 11px; height: 11px; flex: none; }

  .card--back .brand { position: absolute; left: 50%; top: 130px; transform: translateX(-50%); }
  .card--back .brand__dot { width: 46px; height: 46px; background: var(--card-white); }
  .card--back .brand__name { color: var(--card-white); font-size: 34px; font-weight: 300; }
  .web { position: absolute; left: 0; right: 0; bottom: 22px; text-align: center; font-size: 11px; letter-spacing: 0.3px; }
</style>
</head>
<body>
<main class="stage">
  <section class="card card--front" aria-label="Business card front">
    <div class="brand">
      <span class="brand__dot"></span>
      <span class="brand__name">Kindred Path</span>
    </div>
    <div class="person">
      <h1 class="person__name">Derek Hollis</h1>
      <p class="person__role">Counsellor &amp; Psychotherapist</p>
      <p class="person__quals">BSc (Psychol.), BA, Dip. (Couns. &amp; Psych.), PG.Cert (CBT), MGVrA, NWTF</p>
    </div>
    <svg class="divider" viewBox="0 0 424 8" preserveAspectRatio="none" aria-hidden="true">
      <line x1="0" y1="1" x2="424" y2="1" stroke="#4aaee3" stroke-width="1.5"/>
      <polygon points="0,1 8,1 4,7" fill="#4aaee3"/>
    </svg>
    <ul class="contact contact--direct">
      <li><svg viewBox="0 0 12 12"><path d="M2.5 1l2 2-1 1.5c.8 1.6 2 2.8 3.5 3.5L8.5 7l2 2-1.5 2C5 10.5 1.5 7 1 3z" fill="#8cc63f"/></svg>+61 88000 5273</li>
      <li><svg viewBox="0 0 12 12"><rect x="3" y="1" width="6" height="10" rx="1" fill="#8cc63f"/></svg>08-8000-5273</li>
      <li><svg viewBox="0 0 12 12"><rect x="1" y="2.5" width="10" height="7" rx="1" fill="#8cc63f"/><path d="M1.5 3l4.5 3.5L10.5 3" stroke="#fff" fill="none"/></svg>info@brightmindpro.com.au</li>
      <li><svg viewBox="0 0 12 12"><circle cx="6" cy="6" r="5" fill="#8cc63f"/><path d="M1 6h10M6 1c-2 2.5-2 7.5 0 10M6 1c2 2.5 2 7.5 0 10" stroke="#fff" stroke-width=".8" fill="none"/></svg>www.brightmindpro.com.au</li>
    </ul>
    <ul class="contact contact--address">
      <li>Marrowgate, Australia</li>
      <li>12 Banksia Court Fernvale</li>
      <li>Marrowgate, SA 5999</li>
    </ul>
  </section>

  <section class="card card--back" aria-label="Business card back">
    <div class="brand">
      <span class="brand__dot"></span>
      <span class="brand__name">Kindred Path</span>
    </div>
    <p class="web">www.kindredpath.com.au</p>
  </section>
</main>
</body>
</html>
```